Page for a flyer

I need a page designed that is 8.5" wide and 5.5" height. I need the left half of the page to be vintage looking in color and texture and the other half to be plain white and look like it is ripped down the middle

```html
<!DOCTYPE html>
<html lang="en">
<head>
<meta charset="utf-8">
<title>Flyer Page – Vintage and Torn White</title>
<link rel="stylesheet" href="https://fonts.googleapis.com/css2?family=Lora&display=swap">
<style>
  :root {
    --backdrop: #363636;
    --page-white: #ffffff;
    --paper-light: #fcf7e8;
    --paper-mid: #efe4cc;
    --paper-edge: #d9c49e;
    --paper-dark: #c9ad80;
    --tear-shadow: rgba(0, 0, 0, 0.35);
  }
  html, body {
    margin: 0;
    padding: 0;
    width: 1200px;
    height: 1200px;
    overflow: hidden;
    background: var(--backdrop);
    font-family: "Lora", serif;
  }
  .canvas {
    position: relative;
    width: 1200px;
    height: 1200px;
  }
  .flyer-page {
    position: absolute;
    left: 83px;
    top: 261px;
    width: 1033px;
    height: 679px;
    background: var(--page-white);
    box-shadow: 0 10px 30px rgba(0, 0, 0, 0.55);
  }
  .flyer-page svg {
    display: block;
    width: 100%;
    height: 100%;
  }
</style>
</head>
<body>
<main class="canvas">
  <section class="flyer-page" aria-label="Flyer page, vintage left half torn from plain white right half">
    <svg viewBox="0 0 1033 679" xmlns="http://www.w3.org/2000/svg">
      <defs>
        <radialGradient id="aged-paper" cx="0.5" cy="0.25" r="0.85">
          <stop offset="0" stop-color="var(--paper-light)"/>
          <stop offset="0.45" stop-color="var(--paper-mid)"/>
          <stop offset="0.85" stop-color="var(--paper-edge)"/>
          <stop offset="1" stop-color="var(--paper-dark)"/>
        </radialGradient>
        <linearGradient id="edge-burn" x1="0" y1="0" x2="1" y2="0">
          <stop offset="0" stop-color="var(--paper-dark)" stop-opacity="0.45"/>
          <stop offset="0.12" stop-color="var(--paper-dark)" stop-opacity="0"/>
          <stop offset="0.9" stop-color="var(--paper-dark)" stop-opacity="0"/>
          <stop offset="1" stop-color="var(--paper-dark)" stop-opacity="0.3"/>
        </linearGradient>
        <filter id="tear-shadow" x="-5%" y="-5%" width="115%" height="110%">
          <feDropShadow dx="3" dy="1" stdDeviation="2.5" flood-color="var(--tear-shadow)"/>
        </filter>
        <clipPath id="page-clip">
          <rect width="1033" height="679"/>
        </clipPath>
      </defs>

      <g clip-path="url(#page-clip)">
        <path class="torn-half" filter="url(#tear-shadow)" fill="var(--page-white)"
          d="M0 0 H524 L526 8 L523 16 L528 26 L526 36 L530 46 L527 58 L531 70 L528 82
             L530 94 L524 106 L527 118 L532 132 L530 146 L535 158 L532 170 L528 184
             L531 198 L527 212 L530 226 L528 240 L532 256 L529 272 L533 290 L530 306
             L526 320 L529 334 L525 350 L528 366 L523 382 L526 398 L521 414 L525 428
             L522 444 L527 458 L524 472 L528 486 L524 496 L530 502 L532 516 L530 530
             L535 546 L532 560 L537 574 L534 588 L540 600 L537 614 L531 626 L529 640
             L532 654 L528 666 L531 679 H0 Z"/>
        <path class="vintage-paper" role="img" aria-label="Aged vintage paper texture in cream and sepia tones"
          fill="url(#aged-paper)"
          d="M0 0 H521 L523 8 L520 16 L525 26 L523 36 L527 46 L524 58 L528 70 L525 82
             L527 94 L521 106 L524 118 L529 132 L527 146 L532 158 L529 170 L525 184
             L528 198 L524 212 L527 226 L525 240 L529 256 L526 272 L530 290 L527 306
             L523 320 L526 334 L522 350 L525 366 L520 382 L523 398 L518 414 L522 428
             L519 444 L524 458 L521 472 L525 486 L521 496 L527 502 L529 516 L527 530
             L532 546 L529 560 L534 574 L531 588 L537 600 L534 614 L528 626 L526 640
             L529 654 L525 666 L528 679 H0 Z"/>
        <rect class="edge-burn" x="0" y="0" width="530" height="679" fill="url(#edge-burn)"
          style="mix-blend-mode:multiply"/>
      </g>
    </svg>
  </section>
</main>
</body>
</html>
```